Business Card Design

Design new business card using new logo attached and some details as old business card, which is also attached.

Industry/Entity Type

Business

```html
<!DOCTYPE html>
<html lang="en">
<head>
<meta charset="utf-8">
<title>DRW Business Cards</title>
<link rel="stylesheet" href="https://fonts.googleapis.com/css2?family=Cinzel:wght@500;600&family=Lato:wght@400&display=swap">
<style>
  :root {
    --stage: #878787;
    --paper: #ffffff;
    --navy: #252263;
    --navy-glow: #2e3190;
    --slate: #808285;
    --slate-dark: #737578;
    --ink-light: #ffffff;
  }
  html, body {
    margin: 0;
    padding: 0;
    width: 1000px;
    height: 1200px;
    overflow: hidden;
    background: var(--stage);
  }
  .stage {
    position: relative;
    width: 1000px;
    height: 1200px;
    background: var(--stage);
  }
  .card {
    position: absolute;
    left: 138px;
    background: var(--paper);
    overflow: hidden;
  }
  .card--angled { top: 94px; width: 726px; height: 449px; }
  .card--banded { top: 658px; width: 716px; height: 441px; }

  .card__shapes {
    position: absolute;
    inset: 0;
    width: 100%;
    height: 100%;
  }
  .band {
    position: absolute;
    left: 0;
    top: 233px;
    width: 100%;
    height: 208px;
    background: radial-gradient(ellipse 320px 160px at 335px 18px, var(--navy-glow), var(--navy));
  }

  .brand-name {
    position: absolute;
    left: 52px;
    top: 88px;
    width: 210px;
    height: 50px;
    display: flex;
    align-items: center;
    justify-content: center;
    gap: 12px;
  }
  .brand-name__square {
    width: 22px;
    height: 22px;
    background: var(--slate);
  }
  .brand-name__text {
    margin: 0;
    font-family: "Cinzel", serif;
    font-weight: 600;
    font-size: 40px;
    line-height: 1;
    letter-spacing: 2px;
    color: var(--navy);
  }
  .brand-divider {
    position: absolute;
    top: 51px;
    width: 2px;
    height: 121px;
    background: var(--slate);
  }
  .card--angled .brand-divider { left: 280px; }
  .card--banded .brand-divider { left: 276px; }

  .brand-text {
    position: absolute;
    top: 64px;
    font-family: "Cinzel", serif;
  }
  .card--angled .brand-text { left: 310px; }
  .card--banded .brand-text { left: 305px; }
  .brand-text__service {
    margin: 0;
    font-weight: 600;
    font-size: 28px;
    line-height: 35px;
    color: var(--navy);
    letter-spacing: 0.6px;
    text-transform: uppercase;
    white-space: nowrap;
  }
  .brand-text__person {
    margin: 4px 0 0;
    font-weight: 600;
    font-size: 21px;
    line-height: 22px;
    color: var(--slate-dark);
    letter-spacing: 1.4px;
    white-space: nowrap;
  }

  .contact {
    position: absolute;
    top: 294px;
    font-family: "Lato", sans-serif;
    font-size: 15px;
    line-height: 17px;
    color: var(--ink-light);
    font-variant: small-caps;
    letter-spacing: 1.4px;
    white-space: nowrap;
  }
  .contact--address { text-align: right; }
  .card--angled .contact--address { right: calc(726px - 389px); }
  .card--banded .contact--address { right: calc(716px - 337px); }
  .card--angled .contact--lines { left: 432px; }
  .card--banded .contact--lines { left: 379px; }
  .contact p { margin: 0; }
  .contact__phone { font-size: 15px; }
  .contact__tag { font-size: 13px; letter-spacing: 1.4px; text-transform: uppercase; }
  .contact__web { font-size: 12px; letter-spacing: 1.6px; text-transform: uppercase; }

  .contact-divider {
    position: absolute;
    top: 284px;
    width: 1.5px;
    height: 100px;
    background: var(--ink-light);
  }
  .card--angled .contact-divider { left: 409px; }
  .card--banded .contact-divider { left: 357px; }
</style>
</head>
<body>
<main class="stage">

  <section class="card card--angled">
    <svg class="card__shapes" viewBox="0 0 726 449" preserveAspectRatio="none" aria-hidden="true">
      <defs>
        <radialGradient id="angledGlow" cx="240" cy="300" r="320" gradientUnits="userSpaceOnUse">
          <stop offset="0" stop-color="#2e3190"/>
          <stop offset="1" stop-color="#252263"/>
        </radialGradient>
      </defs>
      <polygon points="0,284 726,208 726,221 0,288" fill="#808285"/>
      <polygon points="0,363 726,431 726,447 0,367" fill="#808285"/>
      <polygon points="0,288 726,221 726,431 0,363" fill="url(#angledGlow)"/>
    </svg>

    <div class="brand-name">
      <span class="brand-name__square"></span>
      <p class="brand-name__text">DRW</p>
    </div>
    <span class="brand-divider"></span>
    <div class="brand-text">
      <p class="brand-text__service">Tax, Accounting &amp;<br>Advisory Services</p>
      <p class="brand-text__person">Daniel R. Whitaker, CPA, PA</p>
    </div>

    <div class="contact contact--address">
      <p>240 Harbor Point Ave.</p>
      <p>Seaside Bay,</p>
      <p>FL 32099</p>
    </div>
    <span class="contact-divider"></span>
    <div class="contact contact--lines">
      <p class="contact__phone">(555)301-4417 <span class="contact__tag">office</span></p>
      <p class="contact__phone">(555)862-0193 <span class="contact__tag">mobile</span></p>
      <p class="contact__web">dan@drwtaxpa.com</p>
      <p class="contact__web">www.drwtaxpa.com</p>
    </div>
  </section>

  <section class="card card--banded">
    <div class="band"></div>

    <div class="brand-name">
      <span class="brand-name__square"></span>
      <p class="brand-name__text">DRW</p>
    </div>
    <span class="brand-divider"></span>
    <div class="brand-text">
      <p class="brand-text__service">Tax, Accounting &amp;<br>Advisory Services</p>
      <p class="brand-text__person">Daniel R. Whitaker, CPA, PA</p>
    </div>

    <div class="contact contact--address">
      <p>240 Harbor Point Ave.</p>
      <p>Seaside Bay,</p>
      <p>FL 32099</p>
    </div>
    <span class="contact-divider"></span>
    <div class="contact contact--lines">
      <p class="contact__phone">(555)301-4417 <span class="contact__tag">office</span></p>
      <p class="contact__phone">(555)862-0193 <span class="contact__tag">mobile</span></p>
      <p class="contact__web">dan@drwtaxpa.com</p>
      <p class="contact__web">www.drwtaxpa.com</p>
    </div>
  </section>

</main>
</body>
</html>
```